Flooring & Interior Design showroom

Just bought this business- Kestrel Lane Flooring & Interiors. Love our logo (we are on Kestrel Lane )and colors
Forest green, gold and black
Love that the back lists everything we do. We no longer have plenotilex but need to add in LVP/ SPC and need to take out vantor shadehub logo at the bottom and use the quib logo instead (maybe? open to suggestions)

Not in love with our cards- I want a higher end look
I hate the gradient poop color we have now.
Would love if they were all black - maybe or ??
or had a foil or embossing?

```html
<!DOCTYPE html>
<html lang="en">
<head>
<meta charset="utf-8">
<title>Kestrel Lane Flooring &amp; Interiors — Business Card</title>
<link href="https://fonts.googleapis.com/css2?family=Crimson+Text:wght@400;600;700&display=swap" rel="stylesheet">
<style>
  :root {
    --card-black: #1a1a1a;
    --forest: #034f40;
    --gold: #efe88a;
    --ink-white: #ffffff;
    --mark-green: #2f6a48;
    --page: #ffffff;
  }
  html, body {
    margin: 0;
    padding: 0;
    width: 1200px;
    height: 1200px;
    overflow: hidden;
    background: var(--page);
    font-family: "Crimson Text", Georgia, serif;
  }
  .card {
    position: absolute;
    left: 146px;
    width: 915px;
    height: 523px;
    background: var(--card-black);
    color: var(--ink-white);
    overflow: hidden;
  }
  .card--front { top: 58px; }
  .card--back { top: 626px; }

  .card__base-stripe {
    position: absolute;
    left: 0; right: 0; bottom: 0;
    height: 11px;
    background: var(--gold);
  }

  /* Brand wordmark */
  .brand {
    position: absolute;
    display: flex;
    align-items: center;
    gap: 22px;
    color: var(--gold);
    font-weight: 400;
  }
  .brand__dot {
    width: 34px; height: 34px;
    border-radius: 50%;
    background: var(--mark-green);
    flex: none;
  }
  .brand__name {
    display: flex;
    flex-direction: column;
    line-height: 1;
  }
  .brand__primary { font-size: 46px; letter-spacing: 1px; }
  .brand__secondary { font-size: 19px; letter-spacing: 2px; text-transform: uppercase; margin-top: 14px; }

  .card--front .brand { left: 84px; top: 132px; }

  /* Name band */
  .name-band {
    position: absolute;
    left: 0; right: 0;
    top: 222px;
    height: 104px;
    background: var(--forest);
    border-top: 5px solid var(--gold);
    box-sizing: border-box;
  }
  .name-band__name {
    position: absolute;
    left: 84px; top: 14px;
    margin: 0;
    font-size: 46px;
    font-weight: 700;
    line-height: 1;
    color: var(--gold);
    letter-spacing: 1px;
  }
  .name-band__title {
    position: absolute;
    left: 85px; top: 64px;
    margin: 0;
    font-size: 19px;
    letter-spacing: 2.5px;
    color: var(--ink-white);
  }

  /* Contact grid */
  .contact {
    position: absolute;
    display: flex;
    align-items: center;
    gap: 13px;
    font-size: 20px;
    line-height: 1;
  }
  .contact__icon { width: 25px; height: 25px; flex: none; }
  .contact--office { left: 85px; top: 352px; }
  .contact--mobile { left: 85px; top: 389px; }
  .contact--email  { left: 507px; top: 350px; }
  .contact--fax    { left: 507px; top: 389px; }

  .address {
    position: absolute;
    left: 0; right: 0;
    top: 446px;
    text-align: center;
    font-size: 20px;
    line-height: 29px;
    margin: 0;
  }

  /* Back */
  .card--back .brand { left: 0; right: 0; top: 108px; justify-content: center; }
  .tagline {
    position: absolute;
    left: 358px; top: 198px;
    width: 195px; height: 24px;
    box-sizing: border-box;
    border: 2px solid var(--gold);
    font-size: 14px;
    line-height: 20px;
    text-align: center;
    color: var(--ink-white);
  }
  .divider {
    position: absolute;
    left: 0; right: 0;
    top: 236px;
    height: 5px;
    background: var(--gold);
  }
  .services {
    position: absolute;
    top: 260px;
    margin: 0;
    padding: 0;
    list-style: none;
    font-size: 20px;
    line-height: 28px;
  }
  .services li::before {
    content: "•";
    font-size: 16px;
    margin-right: 7px;
    vertical-align: 2px;
  }
  .services--col1 { left: 74px; }
  .services--col2 { left: 400px; top: 262px; }
  .services--col3 { left: 703px; top: 266px; }

  .web {
    position: absolute;
    left: 78px; top: 452px;
    font-size: 29px;
    margin: 0;
  }
  .hotline {
    position: absolute;
    left: 593px; top: 446px;
    font-size: 36px;
    font-weight: 600;
    letter-spacing: 4px;
    color: var(--gold);
    margin: 0;
  }
</style>
</head>
<body>

<section class="card card--front">
  <div class="brand">
    <span class="brand__dot"></span>
    <span class="brand__name">
      <span class="brand__primary">Kestrel Lane</span>
      <span class="brand__secondary">Flooring &amp; Interiors</span>
    </span>
  </div>

  <div class="name-band">
    <h1 class="name-band__name">MARA LINDEN</h1>
    <p class="name-band__title">OWNER/ DESIGNER</p>
  </div>

  <div class="contact contact--office">
    <svg class="contact__icon" viewBox="0 0 24 24" aria-hidden="true"><circle cx="12" cy="12" r="12" fill="#fff"/><path d="M8.2 6.2l2 2.4-1.2 1.4c.8 1.7 2 2.9 3.7 3.7l1.4-1.2 2.4 2-1.3 2c-3.9-.3-7.6-4-7.9-7.9z" fill="#1a1a1a"/></svg>
    <span>555-214-0387</span>
  </div>
  <div class="contact contact--mobile">
    <svg class="contact__icon" viewBox="0 0 24 24" aria-hidden="true"><circle cx="12" cy="12" r="12" fill="#fff"/><rect x="8.5" y="5.5" width="7" height="13" rx="1.2" fill="#1a1a1a"/><rect x="9.7" y="7" width="4.6" height="8.6" fill="#fff"/></svg>
    <span>555-630-4172</span>
  </div>
  <div class="contact contact--email">
    <svg class="contact__icon" viewBox="0 0 24 24" aria-hidden="true"><circle cx="12" cy="12" r="12" fill="#fff"/><rect x="6" y="8" width="12" height="8.5" fill="none" stroke="#1a1a1a" stroke-width="1.4"/><path d="M6 8l6 5 6-5M6 16.5l4.5-4M18 16.5l-4.5-4" fill="none" stroke="#1a1a1a" stroke-width="1.2"/></svg>
    <span>hello@kestrellaneflooring.com</span>
  </div>
  <div class="contact contact--fax">
    <svg class="contact__icon" viewBox="0 0 24 24" aria-hidden="true"><circle cx="12" cy="12" r="12" fill="#fff"/><rect x="8.5" y="6" width="7" height="4" fill="#1a1a1a"/><rect x="6.5" y="10.5" width="11" height="6" rx="1" fill="#1a1a1a"/><rect x="8.5" y="14.5" width="7" height="3.5" fill="#1a1a1a" stroke="#fff" stroke-width=".8"/></svg>
    <span>555-214-0399</span>
  </div>

  <p class="address">418 Kestrel Lane, Harbor Cove CA 90000<br>CA Lic # 500000</p>

  <div class="card__base-stripe"></div>
</section>

<section class="card card--back">
  <div class="brand">
    <span class="brand__dot"></span>
    <span class="brand__name">
      <span class="brand__primary">Kestrel Lane</span>
      <span class="brand__secondary">Flooring &amp; Interiors</span>
    </span>
  </div>
  <div class="tagline">Home Town Service Since 1979</div>
  <div class="divider"></div>

  <ul class="services services--col1">
    <li>Area Rugs</li>
    <li>Blinds</li>
    <li>Carpet</li>
    <li>Cork</li>
    <li>Hardwood</li>
    <li>Laminate</li>
  </ul>
  <ul class="services services--col2">
    <li>Sheers</li>
    <li>Valances</li>
    <li>Vinyl</li>
    <li>Bed Spreads</li>
    <li>Draperies</li>
    <li>LVP / SPC</li>
  </ul>
  <ul class="services services--col3">
    <li>Fabric</li>
    <li>Motorized Shades</li>
    <li>Pillows</li>
    <li>Shutters</li>
    <li>Upholstery</li>
    <li>Verticals</li>
  </ul>

  <p class="web">www.kestrellaneflooring.com</p>
  <p class="hotline">555-214-0387</p>

  <div class="card__base-stripe"></div>
</section>

</body>
</html>
```